Design and Renovation Company Luxury Business Card

I want to create a luxury business card for a Design and Renovation Firm . We will use our current logo. The company name is 742BUILD. We do not want anything standard. We need a very unique concept.
Please see uploaded inspiration. I really like the textured paper option. I would like the card to be thick with debossing, and/or embossing options. The logo has orange in it but I would like to see the card with and without the orange. I think the orange may make the company feel less high-end. The goal is to elevate the logo not match its vibe per se of the logo. We want something very unique, not standard at all!
I would like a space for :
Logo,
Name,
Position,
Email,
Office number,
Website Address,
Business Address,
Thank you!
Have fun!
Target Market(s)
Home owners Age 35 +
Industry/Entity Type
Design and Renovation
Contact Information for Business Card
Logo, Name, Position, Email, Office number, Website Address, Business Address,.
Colors
Designer to choose colors to be used in the design.
Requirements
Must have
- A luxury designer feel. Must be black or dark grey but open to other luxury ideas.
Nice to have
- Gold, silver, black embossing or debossing. Textured paper design.
Should not have
- A cheap look and feel.

```html
<!DOCTYPE html>
<html lang="en">
<head>
<meta charset="utf-8">
<title>742BUILD Business Card</title>
<link href="https://fonts.googleapis.com/css2?family=Lato:wght@400;700&display=swap" rel="stylesheet">
<style>
  :root {
    --bg: #3a3a3a;
    --card: #1d1d1d;
    --card-front: #1a1a1a;
    --deboss: #111111;
    --white: #ffffff;
    --orange: #f7941d;
    --rule: #d9d9d9;
  }
  * { margin: 0; padding: 0; box-sizing: border-box; }
  html, body {
    width: 1200px; height: 689px; overflow: hidden;
    background: var(--bg);
    font-family: "Lato", Arial, sans-serif;
  }
  .stage { position: relative; width: 1200px; height: 689px; }
  .card {
    position: absolute; top: 190px;
    width: 540px; height: 309px;
    border-radius: 22px;
    overflow: hidden;
  }
  .card-front { left: 40px; background: var(--card-front); }
  .card-back { left: 620px; background: var(--card); }

  /* Front: debossed company name */
  .front-name {
    position: absolute; left: 0; right: 0; top: 122px;
    text-align: center; color: var(--deboss);
    font-size: 56px; font-weight: 700; letter-spacing: 6px; line-height: 1;
  }

  /* Back */
  .brand-name {
    position: absolute; left: 40px; top: 68px;
    color: var(--white); font-size: 42px; font-weight: 700; letter-spacing: 4px; line-height: 1;
  }
  .person { position: absolute; right: 40px; top: 48px; text-align: right; }
  .person-name { color: var(--orange); font-size: 19px; font-weight: 700; letter-spacing: 0.3px; }
  .person-role { color: var(--white); font-size: 13px; margin-top: 4px; }
  .accent-bar { position: absolute; right: 0; top: 46px; width: 10px; height: 34px; background: var(--orange); }
  .divider { position: absolute; left: 40px; right: 30px; top: 162px; height: 1px; background: var(--rule); }

  .contacts { position: absolute; left: 40px; top: 184px; list-style: none; }
  .contacts li { display: flex; align-items: center; gap: 10px; color: var(--white); font-size: 13px; height: 24px; }
  .contacts svg { width: 14px; height: 14px; flex: none; }

  .address {
    position: absolute; right: 40px; top: 190px; text-align: right;
    color: var(--white); font-size: 13px; line-height: 1.6; font-style: normal;
  }
</style>
</head>
<body>
<main class="stage">
  <section class="card card-front" aria-label="Card front">
    <div class="front-name">742BUILD</div>
  </section>

  <section class="card card-back" aria-label="Card back">
    <div class="brand-name">742BUILD</div>

    <div class="accent-bar"></div>
    <div class="person">
      <div class="person-name">DANIEL HARTLEY</div>
      <div class="person-role">Owner</div>
    </div>

    <div class="divider"></div>

    <ul class="contacts">
      <li>
        <svg viewBox="0 0 16 16" aria-hidden="true"><path fill="var(--orange)" d="M3 1.5l2.6-.5 1.4 3.3-1.7 1.3a8 8 0 0 0 4.1 4.1l1.3-1.7 3.3 1.4-.5 2.6c-.2.8-1 1.3-1.8 1.2C6.1 12.6 3.4 9.9 2.8 4.3 2.7 3.5 2.2 1.7 3 1.5z"/></svg>
        071-555 204 318
      </li>
      <li>
        <svg viewBox="0 0 16 16" aria-hidden="true"><rect x="1" y="3.5" width="14" height="10" fill="var(--orange)"/><path d="M1.5 4l6.5 5 6.5-5" fill="none" stroke="var(--card)" stroke-width="1.4"/></svg>
        hello@742build.com
      </li>
      <li>
        <svg viewBox="0 0 16 16" aria-hidden="true"><circle cx="8" cy="8" r="6.8" fill="none" stroke="var(--orange)" stroke-width="1.6"/><ellipse cx="8" cy="8" rx="2.8" ry="6.8" fill="none" stroke="var(--orange)" stroke-width="1.2"/><line x1="1.5" y1="8" x2="14.5" y2="8" stroke="var(--orange)" stroke-width="1.2"/></svg>
        www.742build.com
      </li>
    </ul>

    <address class="address">
      88, Cedar Row Avenue<br>
      30917, Northland
    </address>
  </section>
</main>
</body>
</html>
```